Harbor & Crest Real estate

Design of business plans and presentations before and after of assets is required.
The design is of PowerPoint files and needs to be tailored to the US real estate market.
Graphs and relevant information is required about the area where the company property, Cincinnati Ohio is located.
To get acquainted with the logo, colors and guidelines of the existing company design, visit the website- www.hcqholdings.com

Seeking designer for long term collaborative work.

Font styles to use
Sans Serif

```html
<!DOCTYPE html>
<html lang="en">
<head>
<meta charset="utf-8">
<title>Harrison Project – Plans vs. Execution</title>
<link rel="stylesheet" href="https://fonts.googleapis.com/css2?family=Open+Sans:wght@400;600;700;800&display=swap">
<style>
:root{
  --ink:#0d0d0d;
  --black:#000;
  --white:#fff;
  --yellow:#f7c51e;
  --page:#ececec;
  --grey:#6d6d6d;
  --line:#d9d9d9;
}
*{box-sizing:border-box;margin:0;padding:0}
html,body{width:1200px;height:2250px;overflow:hidden}
body{background:linear-gradient(90deg,#e6e6e6,#fafafa 30%,#fafafa 70%,#e6e6e6);font-family:"Open Sans",Arial,sans-serif;color:var(--ink);position:relative}
.slide{position:absolute;left:336px;width:528px;height:296px;background:var(--white);overflow:hidden;box-shadow:0 4px 14px rgba(0,0,0,.18)}
.rail{position:absolute;left:0;top:0;width:22px;height:100%;background:var(--black);color:var(--white)}
.rail .num{position:absolute;top:8px;width:100%;text-align:center;font-size:6px}
.rail .mark{position:absolute;bottom:8px;width:100%;text-align:center;font-size:5px;font-weight:700;line-height:1.1}
.rail .side{position:absolute;left:50%;top:60px;transform:translateX(-50%) rotate(180deg);writing-mode:vertical-rl;font-size:4px;letter-spacing:.5px;color:#bbb}
.title{position:absolute;left:45px;top:14px;font-size:22px;font-weight:800;letter-spacing:-.2px}
.sub{position:absolute;left:45px;font-size:11px;color:var(--yellow);font-weight:400}
.photo{position:absolute}
.small{font-size:5px;line-height:1.45;color:#333}
/* cover */
.cover .photo{inset:0;background:linear-gradient(90deg,#2a2a2c 0%,#3b3a38 50%,#2d3b4d 60%,#4a5968 100%)}
.cover .frame{position:absolute;inset:9px;border:1.5px solid var(--white)}
.cover .brand{position:absolute;top:64px;width:100%;text-align:center;color:var(--white);font-size:8px;font-weight:700}
.cover .brand span{display:block;font-weight:400;font-size:5px;margin-top:1px}
.cover h1{position:absolute;top:183px;width:100%;text-align:center;color:var(--white);font-size:27px;font-weight:800}
.cover h2{position:absolute;top:218px;width:100%;text-align:center;color:#e8e8e8;font-size:19px;font-weight:400}
/* background */
.bg .photo{left:33px;top:10px;right:10px;bottom:10px;background:linear-gradient(135deg,#3a3530,#2a2623 60%,#3d362f)}
.bg .title{color:var(--white);left:48px}
.bg .sub{left:48px;top:44px}
.cards{position:absolute;left:56px;top:85px;display:flex;gap:12px}
.card{width:84px;height:163px;border:1px solid #cfcfcf;padding:12px 6px;text-align:center;color:var(--white)}
.card .ico{width:30px;height:30px;border-radius:50%;background:var(--white);margin:0 auto 14px;display:flex;align-items:center;justify-content:center}
.card p{font-size:4.8px;line-height:1.5}
/* locating */
.locate .sub{top:46px}
.locate .text{position:absolute;left:45px;top:115px;width:180px}
.locate .text p{margin-bottom:5px}
.aerial{left:232px;top:0;width:138px;height:189px;background:radial-gradient(circle at 60% 40%,#5c7a4a,#3d5636 55%,#6b7060)}
.mapbox{left:375px;top:99px;width:139px;height:189px;background:linear-gradient(160deg,#e8eee6,#dfe7dd 50%,#e9efe8)}
.ring{position:absolute;border:2px solid var(--yellow);border-radius:50%}
/* plans */
.band{position:absolute;left:45px;right:14px;background:var(--black);color:var(--white)}
.plans .band{top:57px;height:84px;display:flex;align-items:center;padding-left:16px}
.status{font-size:8px;font-weight:700;margin-left:10px;width:86px;line-height:1.3}
.stat{margin-left:22px;text-align:center}
.stat b{display:block;color:var(--yellow);font-size:22px;font-weight:700}
.stat span{font-size:5.5px}
.plans .strategy{position:absolute;left:45px;top:158px;width:235px}
.plans .strategy h3{font-size:9px;font-weight:700;margin-bottom:6px}
.plans .strategy p{margin-bottom:4px}
.docback{position:absolute;left:455px;top:145px;width:60px;height:140px;background:var(--black)}
.doc{left:285px;top:152px;width:180px;height:108px;background:linear-gradient(180deg,#fafafa,#eaeaea);border:1px solid #bbb}
.caption{position:absolute;left:330px;top:264px;font-size:5px;color:#444}
/* business plan */
.plan .sub{top:43px}
.budget{position:absolute;left:30px;top:58px}
.label{position:absolute;font-size:6px;color:#333;line-height:1.2}
.kd{position:absolute;left:290px;top:66px;width:224px;border-collapse:collapse;font-size:5.5px}
.kd th{background:var(--black);color:var(--white);text-align:left;padding:3px 4px;font-size:7px}
.kd td{padding:2.4px 4px;border-bottom:1px solid var(--line)}
.kd td:last-child{text-align:right;font-weight:700}
.kd tr:nth-child(even) td{background:#f3f3f3}
.timeline{position:absolute;left:45px;right:14px;background:var(--black);color:var(--white)}
.timeline h4{text-align:center;font-size:7px;font-weight:700;margin-top:6px}
.tl-line{position:absolute;left:20px;right:30px;top:34px;height:1px;background:#888}
.q{position:absolute;top:27px;width:15px;height:15px;border-radius:50%;border:1.5px solid var(--white);background:var(--black);font-size:5px;font-weight:700;display:flex;align-items:center;justify-content:center}
.q-note{position:absolute;top:48px;font-size:4.5px;line-height:1.3;width:50px;color:#ddd}
.plan .timeline{top:189px;height:98px}
/* execution */
.exec .photo{background:linear-gradient(160deg,#cfc9bf,#9d958a)}
.tag{position:absolute;background:var(--black);color:var(--white);font-size:9px;font-weight:800;text-align:center;letter-spacing:.5px}
/* compare */
.compare .timeline{top:57px;height:102px}
.execbox{position:absolute;right:6px;top:52px;width:88px;height:42px;background:var(--yellow);color:var(--ink);padding:4px 6px;font-size:4.5px;line-height:1.35}
.execbox b{display:block;text-align:center;font-size:6px;margin-bottom:2px}
.summary{position:absolute;left:45px;top:184px;width:128px;height:108px;background:var(--yellow);display:flex;align-items:center;justify-content:center;text-align:center;font-size:11px;font-weight:800;line-height:1.25}
.cmp{position:absolute;top:184px;width:168px;border-collapse:collapse;font-size:5px}
.cmp caption{background:var(--yellow);font-size:7px;font-weight:700;padding:2px;margin-bottom:2px}
.cmp th{background:var(--black);color:var(--white);text-align:left;padding:2px 4px;font-size:6px}
.cmp td{padding:1.8px 4px;border-bottom:1px solid var(--line)}
.cmp td:last-child{text-align:right;font-weight:700}
</style>
</head>
<body>

<!-- 1 Cover -->
<section class="slide cover" style="top:12px">
  <div class="photo" role="img" aria-label="Architect sketching plans beside an apartment building exterior"></div>
  <div class="frame"></div>
  <div class="brand">Harbor &amp; Crest<span>Real estate</span></div>
  <h1>Harrison Project</h1>
  <h2>Plans vs. Execution</h2>
</section>

<!-- 2 Background -->
<section class="slide bg" style="top:333px">
  <div class="rail"><div class="num">2</div><div class="side">HARRISON PROJECT · PLANS VS EXECUTION</div><div class="mark">H&amp;C</div></div>
  <div class="photo" role="img" aria-label="Team meeting around a conference table"></div>
  <div class="title" style="top:12px">Harrison Project</div>
  <div class="sub">Background:</div>
  <div class="cards">
    <div class="card"><div class="ico"><svg width="16" height="16" viewBox="0 0 16 16" fill="none" stroke="#000"><circle cx="8" cy="8" r="6"/><circle cx="8" cy="8" r="2"/></svg></div><p>Harbor &amp; Crest is an investment and real estate management company for U.S. assets, providing investors with full service from location, betterment and renovation to ongoing management and sales management.</p></div>
    <div class="card"><div class="ico"><svg width="16" height="16" viewBox="0 0 16 16" fill="none" stroke="#000"><rect x="3" y="4" width="10" height="9"/><path d="M3 7h10M8 4v9"/></svg></div><p>The core of our real estate investment conduct lies first and foremost in locating transactions at the right price, with the central element being to locate assets at prices significantly lower than the market price.</p></div>
    <div class="card"><div class="ico"><svg width="16" height="16" viewBox="0 0 16 16" fill="none" stroke="#000"><circle cx="7" cy="7" r="4"/><path d="M10 10l4 4"/></svg></div><p>Over the years, we have developed a unique method for locating value add assets in growing areas at prices below market prices.</p></div>
    <div class="card"><div class="ico"><svg width="16" height="16" viewBox="0 0 16 16" fill="none" stroke="#000"><rect x="3" y="3" width="10" height="10"/><path d="M6 6h4M6 9h4"/></svg></div><p>Today, the company manages over 500 properties and units in the United States, properties it has fully developed, including purchasing, renovating and building, operating and managing.</p></div>
    <div class="card"><div class="ico"><svg width="16" height="16" viewBox="0 0 16 16" fill="none" stroke="#000"><path d="M3 14V7l5-4 5 4v7z"/><path d="M7 14v-4h2v4"/></svg></div><p>The company's team is made up entirely of company employees, from construction workers to management, enabling us to manage the transaction and adopt a uniform execution model and to save on cost improvement.</p></div>
  </div>
</section>

<!-- 3 Locating -->
<section class="slide locate" style="top:654px">
  <div class="rail"><div class="num">3</div><div class="side">HARRISON PROJECT · PLANS VS EXECUTION</div><div class="mark">H&amp;C</div></div>
  <div class="title" style="top:22px">Harrison Project</div>
  <div class="sub">Locating the transaction:</div>
  <div class="text small">
    <p><b>Our locating system focuses</b> on yielding assets with potential for improvement that are either partially occupied or upgradeable, where the objective is to purchase assets below market prices.</p>
    <p>The properties are <b>located in developing areas</b> and neighborhoods, close to top schools, universities, employment centers and major transport hubs.</p>
    <p>Within the locating system, <b>we have developed unique methods</b> for locating assets that do not exist or are not offered on the market for sale.</p>
    <p><b>The Harrison 2894 Project</b> was located through our field scout, who focused on the Westwood neighborhood, a central neighborhood among the three western neighborhoods in Cincinnati.</p>
    <p>The property located is a multi-family with 16 housing units, with partial occupancy and considerable betterment potential.</p>
  </div>
  <div class="photo aerial" role="img" aria-label="Aerial view of the Westwood neighborhood"><div class="ring" style="left:44px;top:62px;width:40px;height:40px"></div></div>
  <div class="photo mapbox" role="img" aria-label="Street map showing the property location"><div class="ring" style="left:12px;top:66px;width:40px;height:40px;border-width:3px"></div></div>
</section>

<!-- 4 Plans -->
<section class="slide plans" style="top:975px">
  <div class="rail"><div class="num">4</div><div class="side">HARRISON PROJECT · PLANS VS EXECUTION</div><div class="mark">H&amp;C</div></div>
  <div class="title" style="top:18px">Plans</div>
  <div class="band">
    <svg width="26" height="26" viewBox="0 0 26 26" fill="none" stroke="#fff" stroke-width="1.3"><rect x="4" y="5" width="12" height="18"/><rect x="16" y="11" width="7" height="12"/><path d="M7 9h2M11 9h2M7 13h2M11 13h2M7 17h2M11 17h2"/></svg>
    <div class="status">Asset Status at Location Time:</div>
    <div class="stat" style="margin-left:40px"><b>66%</b><span>Occupancy rate</span></div>
    <div class="stat"><b>$ 36K</b><span>Net monthly income</span></div>
    <div class="stat"><b>$ 475K</b><span>Purchase price after negotiation</span></div>
  </div>
  <div class="strategy small">
    <h3>"Value Add" Investment Strategy:</h3>
    <p>Built on the acquisition of assets at prices below their value using the off-market method.</p>
    <p>The plan is to acquire the property, bring in its value by renovating all the units and the common spaces, and house the units at the expected market rent prices.</p>
    <p>After the raising of rents, ongoing management and maintenance will be done efficiently and economically, in such a way that significantly reduces the cost of the complex and improves the profit margins.</p>
    <p>Towards the end of the process, the cash flow from the project will increase and generate higher profits, thus increasing the value of the property.</p>
  </div>
  <div class="docback"></div>
  <div class="photo doc" role="img" aria-label="Settlement statement document"></div>
  <div class="caption">Cost of purchasing asset</div>
</section>

<!-- 5 Business plan -->
<section class="slide plan" style="top:1296px">
  <div class="rail"><div class="num">5</div><div class="side">HARRISON PROJECT · PLANS VS EXECUTION</div><div class="mark">H&amp;C</div></div>
  <div class="title" style="top:12px">Business Plan Expectations</div>
  <div class="sub">Renovation and budget plan</div>
  <svg class="budget" width="240" height="130" viewBox="0 0 240 130">
    <circle cx="70" cy="62" r="34" fill="none" stroke="#111" stroke-width="7"/>
    <path d="M104 62 A34 34 0 0 1 86 92" fill="none" stroke="#f7c51e" stroke-width="7"/>
    <circle cx="70" cy="62" r="27" fill="#f2f2f2"/>
    <g fill="#fff" stroke="#111" stroke-width="1"><circle cx="70" cy="28" r="3"/><circle cx="99" cy="45" r="3"/><circle cx="41" cy="45" r="3"/><circle cx="45" cy="86" r="3"/><circle cx="99" cy="80" r="3"/></g>
    <path d="M70 25V12H100M99 45L115 40M41 45L25 40M45 86L30 100M99 80L120 88" stroke="#555" stroke-width=".6" fill="none"/>
    <text x="70" y="62" text-anchor="middle" font-size="6" font-family="Open Sans, sans-serif">Budget</text>
    <text x="70" y="71" text-anchor="middle" font-size="7" font-weight="700" font-family="Open Sans, sans-serif">$ 138,000</text>
  </svg>
  <div class="label" style="left:115px;top:62px">Replacing roof</div>
  <div class="label" style="left:148px;top:92px">Replacing windows</div>
  <div class="label" style="left:30px;top:92px">HVAC replacement</div>
  <div class="label" style="left:152px;top:140px;width:70px">Renovation of units, kitchens and bathrooms and toilets</div>
  <div class="label" style="left:36px;top:162px;width:70px">Renewal of electrical appliances</div>
  <table class="kd">
    <tr><th colspan="2">Key Data</th></tr>
    <tr><td>Expected total cost</td><td>$613,000</td></tr>
    <tr><td>Expected Gross income (year)</td><td>$118,000</td></tr>
    <tr><td>Expected net income (year)</td><td>$55,400</td></tr>
    <tr><td>Expected net return</td><td>9.69%</td></tr>
    <tr><td>Expected net income (month)</td><td>$4,950</td></tr>
    <tr><td>Betterment length (months)</td><td>6</td></tr>
    <tr><td>Housing length after betterment (months)</td><td>2</td></tr>
  </table>
  <div class="timeline">
    <h4>Project Timeline (Acquisition, Betterment, Housing and Stabilization):</h4>
    <div class="tl-line"></div>
    <div class="q" style="left:80px">Q1</div>
    <div class="q" style="left:180px">Q2</div>
    <div class="q" style="left:280px">Q3</div>
    <div class="q" style="left:380px">Q4</div>
    <div class="q-note" style="left:40px">Renovation and completion of the acquisition</div>
    <div class="q-note" style="left:190px">Completion of renovation and betterment</div>
    <div class="q-note" style="left:290px">Housing and ongoing management</div>
  </div>
</section>

<!-- 6 Execution -->
<section class="slide exec" style="top:1617px">
  <div class="rail"><div class="num">6</div><div class="side">HARRISON PROJECT · PLANS VS EXECUTION</div><div class="mark">H&amp;C</div></div>
  <div class="title" style="top:18px">Execution</div>
  <div class="photo" style="left:45px;top:75px;width:72px;height:72px" role="img" aria-label="Worn interior before renovation"></div>
  <div class="photo" style="left:121px;top:75px;width:72px;height:72px;background:linear-gradient(160deg,#8a6d52,#4a3a2e)" role="img" aria-label="Old staircase before renovation"></div>
  <div class="photo" style="left:197px;top:75px;width:73px;height:152px;background:linear-gradient(160deg,#d8d4cc,#8c877f)" role="img" aria-label="Damaged bathroom before renovation"></div>
  <div class="photo" style="left:45px;top:151px;width:148px;height:76px;background:linear-gradient(160deg,#a9b5bd,#6f7c85)" role="img" aria-label="Old kitchen before renovation"></div>
  <div class="tag" style="left:45px;top:231px;width:225px;height:22px;line-height:22px">BEFORE</div>
  <div class="tag" style="left:286px;top:75px;width:228px;height:22px;line-height:22px">AFTER</div>
  <div class="photo" style="left:286px;top:103px;width:150px;height:74px;background:linear-gradient(160deg,#c4a184,#7a5b46)" role="img" aria-label="Renovated living room"></div>
  <div class="photo" style="left:440px;top:103px;width:74px;height:152px;background:linear-gradient(180deg,#5a8fd6,#c49872 55%,#8a6a4e)" role="img" aria-label="Renovated building exterior"></div>
  <div class="photo" style="left:286px;top:181px;width:74px;height:74px;background:linear-gradient(160deg,#e2ddd6,#a29c94)" role="img" aria-label="Renovated bedroom"></div>
  <div class="photo" style="left:364px;top:181px;width:72px;height:74px;background:linear-gradient(160deg,#b98d62,#6c4c33)" role="img" aria-label="Renovated staircase"></div>
</section>

<!-- 7 Plans vs execution -->
<section class="slide compare" style="top:1938px">
  <div class="rail"><div class="num">7</div><div class="side">HARRISON PROJECT · PLANS VS EXECUTION</div><div class="mark">H&amp;C</div></div>
  <div class="title" style="top:18px">Plans Vs. Execution</div>
  <div class="timeline">
    <h4>Timeline - Plans vs. Execution:</h4>
    <div class="tl-line"></div>
    <div class="q" style="left:80px">Q1</div>
    <div class="q" style="left:180px">Q2</div>
    <div class="q" style="left:280px">Q3</div>
    <div class="q" style="left:380px">Q4</div>
    <svg style="position:absolute;left:110px;top:34px" width="60" height="50"><path d="M10 0V44M32 0V44M54 0V44" stroke="#fff" stroke-dasharray="2 2"/><circle cx="10" cy="44" r="2" fill="#f7c51e"/><circle cx="32" cy="44" r="2" fill="#f7c51e"/><circle cx="54" cy="44" r="2" fill="#f7c51e"/></svg>
    <div class="q-note" style="left:40px">Renovation and completion of the acquisition</div>
    <div class="q-note" style="left:190px">Completion of renovation and betterment</div>
    <div class="q-note" style="left:290px">Housing and ongoing management</div>
    <div class="execbox"><b>Execution</b>In reality, property betterment took 4 months and full reoccupancy took only 1 month from the end of the renovation process.</div>
  </div>
  <div class="summary">Summary table -<br>Timeline - Plans<br>vs. Execution:</div>
  <table class="cmp" style="left:180px">
    <caption>Business Plan Expectations:</caption>
    <tr><th colspan="2">Data</th></tr>
    <tr><td>Expected total cost</td><td>$613,000</td></tr>
    <tr><td>Expected Gross income(year)</td><td>$118,000</td></tr>
    <tr><td>Expected net income(year)</td><td>$55,400</td></tr>
    <tr><td>Expected net return</td><td>9.69%</td></tr>
    <tr><td>Expected net income(month)</td><td>$4,950</td></tr>
    <tr><td>Betterment length(months)</td><td>6</td></tr>
    <tr><td>Housing length after betterment (months)</td><td>2</td></tr>
  </table>
  <table class="cmp" style="left:350px">
    <caption>Actual Performance:</caption>
    <tr><th colspan="2">Key Data</th></tr>
    <tr><td>Expected total cost</td><td>$613,000</td></tr>
    <tr><td>Expected Gross income(year)</td><td>$129,000</td></tr>
    <tr><td>Expected net income(year)</td><td>$77,760</td></tr>
    <tr><td>Expected net return</td><td>12.69%</td></tr>
    <tr><td>Expected net income(month)</td><td>$6,480</td></tr>
    <tr><td>Betterment length(months)</td><td>4</td></tr>
    <tr><td>Housing length after betterment (months)</td><td>1</td></tr>
  </table>
</section>

</body>
</html>
```